Flyer-Design für Verkauf von Designerkleidung
Ich bin mehr als zufrieden, danke für den tollen Flyer, die schnelle Umsetzung und die unkomplizierten Änderungen. 5⭐️
Zielgruppe
Ich verkaufe für Privatpersonen deren gebrauchte Designerkleidung auf verschiedenen Plattformen. Die Zielgruppe ist 40 - 70 Jahre alt.
Aufgabenstellung
-eventuell Text kürzen, Zusammenfassen, übersichtlicher, ansprechender
-ein Flyer mit Vorder- und Rückseite

```html
<!DOCTYPE html>
<html lang="de">
<head>
<meta charset="utf-8">
<title>Flyer – Verkauf von Designerkleidung</title>
<link rel="stylesheet" href="https://fonts.googleapis.com/css2?family=EB+Garamond:ital,wght@1,600&family=Montserrat:wght@400;500&display=swap">
<style>
  :root {
    --taupe: #c9b2a5;
    --title: #d3beb2;
    --white: #ffffff;
    --contact: #cdb5a8;
    --photo-light-a: #f2f2f3;
    --photo-light-b: #dcdcde;
    --photo-grey-a: #e6e7e8;
    --photo-grey-b: #a9a7a4;
    --photo-warm-a: #f3f1ee;
    --photo-warm-b: #d9cbbd;
  }
  * { margin: 0; padding: 0; box-sizing: border-box; }
  html, body { width: 848px; height: 1200px; overflow: hidden; background: var(--white); }
  .flyer { position: relative; width: 848px; height: 1200px; background: var(--white); font-family: "Montserrat", sans-serif; }

  .headline {
    position: absolute; top: 26px; left: 0; width: 848px;
    text-align: center; font-family: "EB Garamond", serif; font-style: italic; font-weight: 600;
    font-size: 42px; line-height: 56px; color: var(--title);
  }

  .tile { position: absolute; }
  .tile--text { background: var(--taupe); color: var(--white); display: flex; flex-direction: column; align-items: center; justify-content: center; text-align: center; }
  .tile p { font-size: 17px; line-height: 24.5px; white-space: nowrap; }
  .tile h2 { font-family: "EB Garamond", serif; font-style: italic; font-weight: 600; font-size: 35px; line-height: 1; margin-bottom: 20px; }

  .intro { left: 0; top: 224px; width: 461px; height: 227px; }
  .commission { left: 461px; top: 453px; width: 387px; height: 244px; padding-top: 8px; }
  .about { left: 0; top: 700px; width: 461px; height: 347px; }
  .about h2 { font-size: 37px; margin-bottom: 18px; }
  .about p { font-size: 16px; line-height: 22.2px; }

  .photo-folded { left: 463px; top: 224px; width: 385px; height: 227px; background: linear-gradient(160deg, var(--photo-light-a), var(--photo-light-b)); }
  .photo-rack { left: 0; top: 453px; width: 459px; height: 244px; background: linear-gradient(135deg, var(--photo-grey-a), var(--photo-grey-b)); }
  .photo-boutique { left: 461px; top: 700px; width: 387px; height: 347px; background: linear-gradient(120deg, var(--photo-warm-a), var(--photo-warm-b)); }

  .call {
    position: absolute; top: 1085px; left: 0; width: 848px; text-align: center;
    font-size: 23.5px; font-weight: 500; letter-spacing: 0.3px; color: var(--contact);
  }
  .contact { position: absolute; top: 1145px; display: flex; align-items: center; gap: 12px; font-size: 23px; color: var(--contact); }
  .contact--phone { left: 90px; }
  .contact--mail { left: 454px; }
  .contact svg { stroke: var(--contact); fill: none; stroke-width: 1.4; }
</style>
</head>
<body>
<div class="flyer">
  <h1 class="headline">Ich verkaufe Ihre Designer- und<br>Markenkleidung für Sie!<br>Sie müssen nichts tun - nur aussortieren.</h1>

  <div class="tile tile--text intro">
    <p>Sie sortieren aus, ich schätze anhand<br>von Marke, Material und Zustand den<br>Wert - stelle sie auf mehreren Plattformen<br>ein - vermesse auf Wunsch und verhandle<br>den Preis mit dem Käufer. Die Käufer<br>zahlen im Voraus, anschließend<br>versende ich den Artikel.</p>
  </div>
  <div class="tile photo-folded" role="img" aria-label="Gefaltete Pullover auf einem weißen Stuhl"></div>

  <div class="tile photo-rack" role="img" aria-label="Jacken auf einer Kleiderstange mit Hut"></div>
  <div class="tile tile--text commission">
    <h2>Meine Provision</h2>
    <p>Meine Provision beträgt 50%.<br>Bei höherpreisigen Kleidungsstücken<br>oder Handtaschen nennen Sie<br>mir gerne Ihre Preisvorstellung.</p>
  </div>

  <div class="tile tile--text about">
    <h2>Über mich</h2>
    <p>Mein Name ist Katrin Selbig, bin 32 Jahre alt,<br>komme aus Lindenau und verkaufe<br>schon seit vielen Jahren Markenkleidung im<br>Internet. Ich habe bereits mehr als 600 positive<br>Bewertunge auf mehreren Plattformen erhalten.<br>Durch meine Expertise in Marken und Materialen<br>kann ich preislich das Beste aushandeln, was<br>möglich ist. Ich dokumentiere jeden Verkauf ganz<br>genau und Sie können auf Wunsch hin jederzeit<br>Einblick in die Gesprächsverläufe nehmen.</p>
  </div>
  <div class="tile photo-boutique" role="img" aria-label="Helle Boutique mit Kleiderstangen und Pflanze"></div>

  <p class="call">Ich freue mich über Ihre Anfrage per Telefon oder per E-Mail!</p>

  <div class="contact contact--phone">
    <svg width="32" height="32" viewBox="0 0 24 24" aria-hidden="true"><path d="M5 3h3.5l1.8 4.5-2.3 1.6a11 11 0 0 0 6.9 6.9l1.6-2.3L21 15.5V19a2 2 0 0 1-2 2A17 17 0 0 1 3 5a2 2 0 0 1 2-2z"/></svg>
    <span>0151 2384 716</span>
  </div>
  <div class="contact contact--mail">
    <svg width="34" height="26" viewBox="0 0 34 26" aria-hidden="true"><rect x="1" y="1" width="32" height="24"/><path d="M1 1l16 13L33 1M1 25l12-12M33 25L21 13"/></svg>
    <span>katrinselbig@postfach.de</span>
  </div>
</div>
</body>
</html>
```